Lost & Found Website - PAYMENT GUARANTY

PC website and Mobile Website

Our website aims to develop an online management platform for lost & found objects with the use of stickers.
This solution allows users to buy stickers which will be affixed on the owners’ objects (glasses, laptops, phones …).
Users shall register the code on the website or the mobile application (flashing QR code). Platform will alert by email users if its object is found.
The person who finds an object with a sticker will be encouraged to declare the code on the web/mobile site. Once the object is found, it is identified by the system and the platform notifies the owner via email and give access to contact details of the person who found the object.

PLEASE SEE REQUIREMENT ATTACHED
Updates

Project Deadline Extended
Reason: We are waiting for more interesting ideas. Thank you all for your work. B. Lorimond

Project Deadline Extended
Reason: Your designs are very next to perfection !

Target Market(s)

Our target are people 20 to 35 years old who care about there objects. Mainly French market at the beginning.

Industry/Entity Type

Management

Requirements
Must have
• Specifications:

The design must follow basic web design rules:
- Consistent site header/logo
- Page footer area includes copyright, last update, contact e-mail address
- Color scheme is limited to a maximum of three or four colors plus neutrals
- Color is used consistently
- Common fonts such as Arial or Times New Roman are used
- No more than one web font is used
- Fonts, font sizes, and font colors are consistently used
- Information is easy to find (minimal clicks)
- Find a suitable place to put the sponsor's logos.

For mobile version, we need a design that can fit to any screen size,
so please create standard mobile design.
Nice to have
• The website should allow users to:
- Create an account
- Buy lots of stickers
- Associate stickers to their objects
- Report the loss of an object by email
- Access full contact information of the finder after he paid the service
- Declare a found object
- The payment process management via Quidora platform
Should not have
• Only PSD files.

No html.

```html
<!DOCTYPE html>
<html lang="en">
<head>
<meta charset="utf-8">
<title>Trovano – Mobile Screens</title>
<link rel="stylesheet" href="https://fonts.googleapis.com/css2?family=Noto+Sans:wght@400;700&display=swap">
<style>
  :root {
    --canvas: #333333;
    --white: #ffffff;
    --ink: #111111;
    --nav: #8eafc9;
    --nav-soft: #9fb9cf;
    --field-border: #5aaaf0;
    --btn-blue: #5b8bb5;
    --btn-red: #e00000;
    --map-deep: #1f3550;
    --map-mid: #4a6a8c;
    --sticker-bg: #8aa3bc;
    --select-bg: #bdbdbd;
    --pay-bg: #444444;
    --caption: #9a9a9a;
  }
  * { box-sizing: border-box; margin: 0; padding: 0; }
  html, body { width: 1200px; height: 1000px; overflow: hidden; }
  body { background: var(--canvas); font-family: "Noto Sans", Verdana, sans-serif; color: var(--ink); position: relative; }

  .screen { position: absolute; overflow: hidden; }
  .screen > * { position: absolute; }

  .brand { left: 0; right: 0; display: flex; align-items: center; justify-content: center; gap: 8px; font-weight: 400; color: var(--ink); }
  .brand-dot { width: 8px; height: 8px; border-radius: 50%; background: var(--ink); }

  .nav { left: 0; right: 0; background: var(--nav); display: flex; justify-content: center; align-items: center; }
  .nav a { color: var(--ink); text-decoration: underline; }

  .field { border: 2px solid var(--field-border); border-radius: 5px; background: linear-gradient(#fafafa, #b8b8b8); }
  .label { font-size: 13px; }

  .btn { color: var(--white); font-weight: 700; text-align: center; border-radius: 3px; }
  .btn-blue { background: var(--btn-blue); }
  .btn-red { background: var(--btn-red); }

  /* mobile home */
  .home { left: 161px; top: 318px; width: 218px; height: 378px; background: #b4b4b4; }
  .home .header { left: 0; top: 0; width: 218px; height: 54px; background: linear-gradient(#ffffff, #d6d6d6); }
  .home .brand { top: 8px; height: 40px; font-size: 26px; }
  .home .nav { top: 54px; height: 24px; gap: 22px; font-size: 11px; background: var(--nav-soft); }
  .home .nav a:last-child { color: #333; }
  .home .intro { left: 7px; top: 81px; width: 206px; font-size: 10px; line-height: 13px; color: #222; }
  .home .world { left: 0; top: 112px; width: 218px; height: 266px; }
  .home .field { left: 23px; width: 163px; height: 30px; font-size: 11px; padding: 7px 8px; border-radius: 4px; }
  .home .login { left: 24px; top: 228px; width: 81px; height: 22px; font-size: 11px; line-height: 22px; }
  .home .social { left: 129px; top: 227px; font-size: 10px; line-height: 12px; color: var(--white); }
  .home .btn-wide { left: 24px; width: 163px; height: 22px; font-size: 11px; line-height: 22px; }

  /* flat pages */
  .page { width: 320px; height: 600px; background: linear-gradient(#ffffff 18%, #b0b0b0); }
  .page .header { left: 0; top: 0; width: 320px; height: 72px; background: var(--white); }
  .page .brand { top: 14px; height: 46px; font-size: 32px; }
  .page .nav { top: 72px; height: 28px; gap: 24px; font-size: 13px; }
  .page .btn-wide { left: 58px; width: 201px; height: 27px; font-size: 14px; line-height: 27px; }

  .found { left: 489px; top: 199px; }
  .found .nav { top: 72px; }
  .found .label { left: 57px; }
  .found .field { left: 56px; width: 204px; height: 30px; }
  .found .code { font-size: 18px; font-weight: 700; padding: 2px 12px; letter-spacing: 0.5px; }
  .found .send { left: 123px; top: 434px; width: 76px; height: 26px; font-size: 15px; line-height: 26px; }

  .cart { left: 838px; top: 200px; }
  .cart .sticker { left: 78px; top: 122px; width: 160px; height: 101px; background: var(--sticker-bg); }
  .cart .details { left: 35px; top: 235px; width: 260px; font-size: 13px; line-height: 18px; }
  .cart .details strong { letter-spacing: 0.5px; }
  .cart .select { top: 302px; height: 30px; background: var(--select-bg); border-radius: 4px; font-size: 11px; display: flex; align-items: center; justify-content: space-between; padding: 0 4px 0 11px; }
  .cart .total-label { left: 0; right: 0; top: 350px; text-align: center; font-size: 13px; }
  .cart .total { left: 0; right: 0; top: 368px; text-align: center; font-size: 18px; font-weight: 700; }
  .cart .pay { left: 58px; top: 407px; width: 201px; height: 29px; background: var(--pay-bg); color: var(--white); font-size: 14px; display: flex; align-items: center; justify-content: center; gap: 8px; }
  .cart .pay strong { font-size: 18px; }

  .caption { position: absolute; width: 320px; text-align: center; font-size: 14px; color: var(--caption); top: 816px; letter-spacing: 0.3px; }
</style>
</head>
<body>

  <!-- Mobile home screen -->
  <section class="screen home">
    <div class="header"></div>
    <div class="brand"><span class="brand-dot"></span>Trovano</div>
    <nav class="nav"><a>Home</a><a>About</a><a>Buy</a><a>Contact</a></nav>
    <p class="intro"><strong>Trovano</strong> is lost &amp; found service for people and businesses all around the world.</p>
    <svg class="world" viewBox="0 0 218 266" role="img" aria-label="World map background in deep blue tones">
      <defs>
        <radialGradient id="worldTone" cx="50%" cy="45%" r="70%">
          <stop offset="0" stop-color="#4a6a8c"/>
          <stop offset="1" stop-color="#1f3550"/>
        </radialGradient>
      </defs>
      <path d="M0 40 Q109 -10 218 40 L218 266 L0 266 Z" fill="url(#worldTone)"/>
      <path d="M0 40 Q109 -10 218 40" fill="none" stroke="#e8e8e8" stroke-width="2"/>
    </svg>
    <div class="field" style="top:153px">Username</div>
    <div class="field" style="top:190px">Password</div>
    <div class="btn btn-red login">LOGIN</div>
    <div class="social">Login with<br><strong>Chirpa</strong></div>
    <div class="btn btn-blue btn-wide" style="top:290px">Create New Account</div>
    <div class="btn btn-blue btn-wide" style="top:319px">Found Item?</div>
    <div class="btn btn-red btn-wide" style="top:348px">REGISTER CODE</div>
  </section>

  <!-- Found form page -->
  <section class="screen page found">
    <div class="header"></div>
    <div class="brand"><span class="brand-dot"></span>Trovano</div>
    <nav class="nav"><a>Home</a><a>About</a><a>Buy</a><a>Contact</a></nav>
    <span class="label" style="top:110px">Retrova Code</span>
    <div class="field code" style="top:135px">G3IRSD</div>
    <span class="label" style="top:173px">Name</span>
    <div class="field" style="top:197px"></div>
    <span class="label" style="top:236px">Telephone</span>
    <div class="field" style="top:260px"></div>
    <span class="label" style="top:300px">Email</span>
    <div class="field" style="top:324px"></div>
    <span class="label" style="top:364px">Message</span>
    <div class="field" style="top:388px"></div>
    <div class="btn btn-blue send">SEND</div>
    <div class="btn btn-blue btn-wide" style="top:485px">Create New Account</div>
    <div class="btn btn-blue btn-wide" style="top:521px">Found Item?</div>
    <div class="btn btn-red btn-wide" style="top:558px">REGISTER CODE</div>
  </section>
  <p class="caption" style="left:489px">FOUND FORM PAGE</p>

  <!-- Cart page -->
  <section class="screen page cart">
    <div class="header"></div>
    <div class="brand"><span class="brand-dot"></span>Trovano</div>
    <nav class="nav"><a>Home</a><a>About</a><a>Buy</a><a>Contact</a></nav>
    <div class="sticker" role="img" aria-label="Sticker kit product image"></div>
    <p class="details"><strong>DETAILS</strong><br>Lorem ipsum dolor sit amet, consectetur auctor hendrerit, erat orci.</p>
    <div class="select" style="left:35px;width:162px">KIT TYPE
      <svg width="24" height="24" viewBox="0 0 24 24"><circle cx="12" cy="12" r="11" fill="#999" stroke="#333" stroke-width="1.5"/><path d="M6 9 L12 17 L18 9" fill="none" stroke="#333" stroke-width="2"/></svg>
    </div>
    <div class="select" style="left:208px;width:79px">QTY
      <svg width="24" height="24" viewBox="0 0 24 24"><circle cx="12" cy="12" r="11" fill="#999" stroke="#333" stroke-width="1.5"/><path d="M6 9 L12 17 L18 9" fill="none" stroke="#333" stroke-width="2"/></svg>
    </div>
    <p class="total-label">YOUT TOTAL</p>
    <p class="total">15EUR</p>
    <div class="pay">Pay With <strong>Quidora</strong></div>
    <div class="btn btn-blue btn-wide" style="top:489px">Create New Account</div>
    <div class="btn btn-blue btn-wide" style="top:525px">Found Item?</div>
    <div class="btn btn-red btn-wide" style="top:562px">REGISTER CODE</div>
  </section>
  <p class="caption" style="left:838px">CART PAGE</p>

</body>
</html>
```